Redesign our business card for more impact

We want to completely replace the back design of our card, and refresh or even change the front entirely. We are happy with our black Q7 logo and do not want to change it.
Our company address changed too. It is now 58 Corvallen, Irvine, CA 92741
Updates

It was reported by Sketch Harbor email today that the uploaded files didnt upload. I am trying again.

Target Market(s)

Architects and Building Owners (People making multi-million dollar decisions)

Industry/Entity Type

Consulting Engineering

Contact Information for Business Card

Contact info on the front. "wallpaper" design on back with tag line on the back "Engineering Your Future"

Font styles to use
Sans Serif

Requirements
Must have
• A vivid, modern, impactful ...but tasteful back of card design. It should communicate our premier status, but grab attention as innovative. DESIGN SHOULD BE ELEGANT AND NOT TOO BUSY.
Nice to have
• Repeating pattern, multi-color, something creative...
Should not have
• Anything that looks too playful or that we are not serious professionals. It should also not be too boring or conservative.

```html
<!DOCTYPE html>
<html lang="en">
<head>
<meta charset="utf-8">
<title>Q7 Business Card</title>
<link rel="stylesheet" href="https://fonts.googleapis.com/css2?family=Open+Sans:wght@400;700&family=Montserrat:ital,wght@1,700&display=swap">
<style>
  :root {
    --backdrop: #cacaca;
    --card-light: #ffffff;
    --card-dark: #333333;
    --ink: #2b2b2b;
    --ink-soft: #7b7b7b;
    --rule: #8a8a8a;
    --white: #ffffff;
  }
  html, body {
    margin: 0;
    padding: 0;
    width: 1126px;
    height: 1200px;
    overflow: hidden;
    background: var(--backdrop);
    font-family: "Open Sans", Arial, sans-serif;
  }
  .card {
    position: absolute;
    left: 150px;
    width: 825px;
    height: 471px;
    border-radius: 26px;
    overflow: hidden;
  }
  .card--front { top: 98px; background: var(--card-light); }
  .card--back  { top: 631px; background: var(--card-dark); }

  .wordmark {
    position: absolute;
    font-weight: 700;
    line-height: 1;
    letter-spacing: -4px;
    margin: 0;
  }
  .card--front .wordmark {
    right: 66px;
    top: 31px;
    font-size: 150px;
    color: var(--ink);
  }
  .card--back .wordmark {
    left: 0;
    right: 0;
    top: 88px;
    text-align: center;
    font-size: 220px;
    letter-spacing: -6px;
    color: var(--white);
  }
  .tagline {
    position: absolute;
    left: 0;
    right: 0;
    top: 330px;
    text-align: center;
    margin: 0;
    font-family: "Montserrat", Arial, sans-serif;
    font-style: italic;
    font-weight: 700;
    font-size: 20.5px;
    line-height: 1.2;
    color: var(--white);
  }

  .identity {
    position: absolute;
    left: 65px;
    top: 275px;
  }
  .identity__name {
    margin: 0;
    font-size: 24px;
    font-weight: 700;
    color: var(--ink);
    line-height: 1.1;
  }
  .identity__role {
    margin: 2px 0 0;
    font-size: 20.5px;
    color: var(--ink-soft);
    line-height: 1.2;
  }
  .identity__role .divider { color: var(--ink); font-weight: 700; }
  .address {
    position: absolute;
    left: 65px;
    top: 362px;
    margin: 0;
    font-size: 20.5px;
    color: var(--ink-soft);
  }
  .contact-rule {
    position: absolute;
    left: 65px;
    right: 66px;
    top: 400px;
    height: 0;
    border-top: 1.5px solid var(--rule);
  }
  .contact-list {
    position: absolute;
    left: 65px;
    right: 66px;
    top: 405px;
    display: flex;
    justify-content: space-between;
    align-items: center;
    font-size: 20.5px;
    color: var(--ink-soft);
  }
  .contact-item { display: flex; align-items: center; gap: 6px; }
  .contact-item svg { width: 14px; height: 14px; fill: var(--ink); }
  .contact-item--mail { gap: 18px; }
  .contact-item--web { gap: 20px; }
</style>
</head>
<body>
  <section class="card card--front">
    <p class="wordmark">Q7</p>
    <div class="identity">
      <h1 class="identity__name">DANIEL WHITCOMBE, PE</h1>
      <p class="identity__role">HFDP, LEED AP <span class="divider">|</span> CEO/Principal</p>
    </div>
    <p class="address">58 Corvallen, Irvine, CA 92741</p>
    <div class="contact-rule"></div>
    <div class="contact-list">
      <span class="contact-item">
        <svg viewBox="0 0 16 16" aria-hidden="true"><path d="M1 6c0-2 3-4 7-4s7 2 7 4v1h-4V5.5H5V7H1z M3 8h10l1 6H2z"/></svg>
        (555) 014-2290
      </span>
      <span class="contact-item contact-item--mail">
        <svg viewBox="0 0 16 16" aria-hidden="true"><path d="M1 6l7-5 7 5v9H1z M2.5 6.5L8 10l5.5-3.5L8 3z" fill-rule="evenodd"/></svg>
        d.whitcombe@q7eng.com
      </span>
      <span class="contact-item contact-item--web">
        <svg viewBox="0 0 16 16" aria-hidden="true"><circle cx="8" cy="8" r="7"/></svg>
        q7eng.com
      </span>
    </div>
  </section>

  <section class="card card--back">
    <p class="wordmark">Q7</p>
    <p class="tagline">Engineering Your Future</p>
  </section>
</body>
</html>
```